Children's Party Business needs a Business Card design!

We need a double sided, colour business card design.
The company name is "Bright Lantern Kids Events". We want one side to feature this logo.
We want the second side to feature the two branches "The Caped Crusade Adventure" and "The Fairy Glade Adventure". I have attached logos for each of these below. When using these, I suggest removing the tagline & image from the logos, as those elements are already featured in the "Bright Lantern Kids Event" logo.
To be included:
www.brightlanternkidsevents.com.au
1300 481 607
Optional text- "Making Dreams a Reality"
Optional photos- I've attached a bunch of our Character photos, which can be used if you please!
To give you an idea of the business, see The Caped Crusade Adventure website (under development):
http://qorvintel.com/demo/capedcrusadeadventure/
Target Market(s)
Parents
Industry/Entity Type
Business
Contact Information for Business Card
To be included:
1300 481 607
Colors
Designer to choose colors to be used in the design.
Look and feel

```html
<!DOCTYPE html>
<html lang="en">
<head>
<meta charset="utf-8">
<title>Bright Lantern Kids Events – Business Card</title>
<link href="https://fonts.googleapis.com/css2?family=Raleway:wght@400;600;800&display=swap" rel="stylesheet">
<style>
  :root {
    --navy: #1f3170;
    --navy-light: #2a4490;
    --white: #ffffff;
    --sky: #6cb8e8;
    --grey: #4a4a55;
    --orange: #f28a2e;
    --lilac: #a48fd8;
    --stage: #2b2b2e;
  }
  * { margin: 0; padding: 0; box-sizing: border-box; }
  html, body {
    width: 1200px; height: 900px; overflow: hidden;
    background: var(--stage);
    font-family: "Raleway", Arial, sans-serif;
  }
  .canvas {
    width: 1200px; height: 900px;
    display: flex; flex-direction: column;
    align-items: center; justify-content: center; gap: 60px;
  }
  .card {
    position: relative;
    width: 600px; height: 343px;
    overflow: hidden;
    box-shadow: 0 12px 30px rgba(0,0,0,.45);
  }

  /* Front */
  .card--front {
    background: radial-gradient(circle at 45% 35%, var(--navy-light), var(--navy) 70%);
    display: flex; align-items: center; justify-content: center; gap: 22px;
  }
  .front__figure {
    width: 110px; height: 96px; border-radius: 10px;
    background: linear-gradient(135deg, var(--lilac), var(--white));
    opacity: .85; flex: none;
  }
  .front__branches { display: flex; flex-direction: column; gap: 14px; }
  .front__brand {
    color: var(--white); font-weight: 800;
    font-size: 26px; line-height: 1.05; letter-spacing: .5px;
  }
  .front__rule { width: 60px; height: 2px; background: var(--sky); }

  /* Back */
  .card--back { background: var(--white); }
  .back__shapes { position: absolute; inset: 0; }
  .back__logo {
    position: absolute; top: 28px; left: 0; right: 0;
    display: flex; justify-content: center; align-items: center; gap: 12px;
  }
  .back__art {
    width: 92px; height: 70px; border-radius: 8px;
    background: linear-gradient(135deg, #e2458f, #5bc4d8 55%, var(--navy));
  }
  .back__brand {
    color: var(--navy); font-weight: 800; font-size: 22px; line-height: 1.1;
  }
  .back__name {
    position: absolute; top: 118px; width: 100%; text-align: center;
    color: var(--sky); font-size: 22px; font-weight: 600; letter-spacing: 1px;
  }
  .back__role {
    position: absolute; top: 146px; width: 100%; text-align: center;
    color: var(--grey); font-size: 12px; letter-spacing: 1.5px;
  }
  .back__icons {
    position: absolute; top: 168px; left: 0; right: 0;
    display: flex; justify-content: center; gap: 8px;
  }
  .contact {
    position: absolute; width: 100%; text-align: center; font-size: 13px;
  }
  .contact--phone { top: 188px; color: var(--grey); }
  .contact--email { top: 236px; color: var(--white); }
  .contact--web { top: 256px; color: var(--white); }
  .back__address {
    position: absolute; left: 22px; top: 314px;
    color: var(--white); font-size: 13px; font-weight: 600; letter-spacing: .5px;
  }
</style>
</head>
<body>
<main class="canvas">

  <section class="card card--front">
    <div class="front__figure" role="img" aria-label="Fairy silhouette illustration"></div>
    <div class="front__branches">
      <div class="front__brand">The Fairy Glade<br>Adventure</div>
      <div class="front__rule"></div>
      <div class="front__brand">The Caped Crusade<br>Adventure</div>
    </div>
  </section>

  <section class="card card--back">
    <svg class="back__shapes" width="600" height="343" viewBox="0 0 600 343">
      <polygon points="0,245 600,190 600,343 0,343" fill="var(--navy)"/>
      <polygon points="0,298 540,298 515,343 0,343" fill="var(--orange)"/>
    </svg>

    <div class="back__logo">
      <div class="back__art" role="img" aria-label="Balloons and party character illustration"></div>
      <div class="back__brand">Bright Lantern<br>Kids Events</div>
    </div>

    <div class="back__name">DANA WHITLOCK</div>
    <div class="back__role">DIRECTOR</div>

    <div class="back__icons">
      <svg width="12" height="12" viewBox="0 0 24 24" aria-label="Phone"><path fill="var(--orange)" d="M6.6 10.8a15 15 0 0 0 6.6 6.6l2.2-2.2a1 1 0 0 1 1-.25 11.4 11.4 0 0 0 3.6.57 1 1 0 0 1 1 1V20a1 1 0 0 1-1 1A17 17 0 0 1 3 4a1 1 0 0 1 1-1h3.5a1 1 0 0 1 1 1c0 1.250.2 2.45.57 3.6a1 1 0 0 1-.25 1z"/></svg>
      <svg width="12" height="12" viewBox="0 0 24 24" aria-label="Email"><rect x="2" y="5" width="20" height="14" rx="2" fill="none" stroke="var(--orange)" stroke-width="2"/><path d="M2 6l10 7 10-7" fill="none" stroke="var(--orange)" stroke-width="2"/></svg>
      <svg width="12" height="12" viewBox="0 0 24 24" aria-label="Website"><circle cx="12" cy="12" r="10" fill="none" stroke="var(--orange)" stroke-width="2"/><path d="M2 12h20M12 2c3 3 3 17 0 20M12 2c-3 3-3 17 0 20" fill="none" stroke="var(--orange)" stroke-width="1.5"/></svg>
    </div>

    <div class="contact contact--phone">1300 481 607</div>
    <div class="contact contact--email">info@brightlanternkidsevents.com.au</div>
    <div class="contact contact--web">www.brightlanternkidsevents.com.au</div>

    <div class="back__address">2817A Ridge Line Rd 14, Maple Vale County, AB, T0K 2L0</div>
  </section>

</main>
</body>
</html>
```